Business Card Design for Varnok Facility Services

We are looking for a Business Card Design for the Company "Varnok Facility Services."
Front side:
- Company Logo (small)
- Company Name, address, pohone, website and personal data.
- white background, for text e.g. company colors (blue or green like in the logo)
Please use following data:
Company data:
Varnok Facility Services Tulbrecht
Kirchmattweg 12
6331 Cham
www.varnok-fs.ch
Person data:
Ruben Tulbrecht
Geschäftsführer
+41 76 519 84 60
info@varnok-fs.ch
Back side:
could be colored in blue or green
please use a big logo sing and some smaller icons to say what is all beeing offered in facility services, like cleaning, maintenance cleaning
industrial cleaning, caretaking, gardening, disposal. There is no need for everyone of the icons if there are similar or an icon is standing for more of them.
Cleaning Service
colors to use:
blue: HEX 246BB0
green: HEX 52B33E

```html
<!DOCTYPE html>
<html lang="de">
<head>
<meta charset="UTF-8">
<title>Varnok Facility Services – Visitenkarte</title>
<link href="https://fonts.googleapis.com/css2?family=Montserrat:wght@400;500;600;700&display=swap" rel="stylesheet">
<style>
  :root {
    --brand-blue: #246BB0;
    --brand-green: #52B33E;
    --grad-green: #4CAA4E;
    --grad-teal: #3E8E8A;
    --grad-blue: #3C78B6;
    --ink: #3a3a3a;
    --paper: #ffffff;
    --stage: #e6e7e9;
  }
  * { box-sizing: border-box; margin: 0; padding: 0; }
  html, body {
    width: 1200px; height: 900px; overflow: hidden;
    background: var(--stage);
    font-family: "Montserrat", sans-serif;
  }
  .card {
    position: absolute;
    left: 300px;
    width: 600px; height: 360px;
    box-shadow: 0 6px 18px rgba(0,0,0,.18);
  }
  /* Back side */
  .card-back {
    top: 50px;
    background: linear-gradient(20deg, var(--grad-green) 0%, var(--grad-teal) 50%, var(--grad-blue) 100%);
    color: var(--paper);
    display: flex; flex-direction: column; align-items: center; justify-content: center;
  }
  .back-brand {
    display: flex; align-items: center; gap: 16px;
    margin-top: 20px;
  }
  .back-brand .mark-dot {
    width: 26px; height: 26px; border-radius: 50%;
    background: var(--paper);
  }
  .back-brand .brand-name {
    font-weight: 600; font-size: 34px; letter-spacing: 1px; line-height: 1.1;
    text-align: center;
  }
  .service-icons {
    display: flex; gap: 86px; margin-top: 42px;
  }
  .service-icons svg { width: 34px; height: 34px; }

  /* Front side */
  .card-front {
    top: 470px;
    background: var(--paper);
    color: var(--ink);
  }
  .front-brand {
    position: absolute; left: 36px; top: 46px;
    display: flex; align-items: center; gap: 10px;
  }
  .front-brand .mark-dot {
    width: 16px; height: 16px; border-radius: 50%;
    background: var(--brand-blue);
  }
  .front-brand .brand-name {
    font-weight: 600; font-size: 19px; color: var(--brand-blue); letter-spacing: .5px;
  }
  .divider {
    position: absolute; left: 40px; right: 40px; top: 200px;
    height: 1px; background: var(--brand-green);
  }
  .person {
    position: absolute; right: 40px; top: 150px; text-align: right;
  }
  .person-name { font-weight: 600; font-size: 16px; letter-spacing: .5px; }
  .person-name .first { color: var(--brand-blue); }
  .person-name .last { color: var(--brand-green); }
  .person-role { font-size: 14px; margin-top: 3px; }
  .contact-list {
    position: absolute; left: 40px; top: 222px;
    list-style: none; font-size: 15px;
  }
  .contact-list li {
    display: flex; align-items: center; gap: 12px; height: 26px;
  }
  .contact-list svg { width: 15px; height: 15px; flex: none; }
  .address {
    position: absolute; right: 40px; bottom: 34px;
    text-align: right; font-size: 16px; line-height: 1.5;
  }
</style>
</head>
<body>

<section class="card card-back" aria-label="Rückseite der Visitenkarte">
  <div class="back-brand">
    <span class="mark-dot"></span>
    <span class="brand-name">Varnok Facility Services</span>
  </div>
  <div class="service-icons">
    <svg role="img" aria-label="Symbol Reinigung" viewBox="0 0 34 34"><circle cx="17" cy="17" r="15.5" fill="none" stroke="#fff" stroke-width="1.5"/></svg>
    <svg role="img" aria-label="Symbol Unterhaltsreinigung" viewBox="0 0 34 34"><circle cx="17" cy="17" r="15.5" fill="none" stroke="#fff" stroke-width="1.5"/></svg>
    <svg role="img" aria-label="Symbol Entsorgung" viewBox="0 0 34 34"><circle cx="17" cy="17" r="15.5" fill="none" stroke="#fff" stroke-width="1.5"/></svg>
  </div>
</section>

<section class="card card-front" aria-label="Vorderseite der Visitenkarte">
  <div class="front-brand">
    <span class="mark-dot"></span>
    <span class="brand-name">Varnok Facility Services</span>
  </div>

  <div class="person">
    <p class="person-name"><span class="first">RUBEN</span> <span class="last">TULBRECHT</span></p>
    <p class="person-role">Geschäftsführer</p>
  </div>

  <div class="divider"></div>

  <ul class="contact-list">
    <li>
      <svg viewBox="0 0 16 16" aria-hidden="true"><path fill="#2f8a86" d="M3.6 1.2l2.2 2.6-1.3 1.6c.8 1.8 2.3 3.3 4.1 4.1l1.6-1.3 2.6 2.2-1 2.4C7 12.6 3.4 9 3.2 4.2z"/></svg>
      <span>+41 76 519 84 60</span>
    </li>
    <li>
      <svg viewBox="0 0 16 16" aria-hidden="true"><rect x="1" y="3" width="14" height="10" rx="1" fill="#2f8a86"/><path d="M1.5 3.8L8 9l6.5-5.2" fill="none" stroke="#fff" stroke-width="1.2"/></svg>
      <span>info@varnok-fs.ch</span>
    </li>
    <li>
      <svg viewBox="0 0 16 16" aria-hidden="true"><circle cx="8" cy="8" r="7" fill="#2f8a86"/><ellipse cx="8" cy="8" rx="3" ry="7" fill="none" stroke="#fff" stroke-width="1"/><path d="M1 8h14" stroke="#fff" stroke-width="1"/></svg>
      <span>www.varnok-fs.ch</span>
    </li>
  </ul>

  <address class="address" style="font-style:normal">
    Kirchmattweg 12<br>
    6331 Cham
  </address>
</section>

</body>
</html>
```